Web Design Project

Need a start website for a new company called TideMarsh.

We help large data center customers optimize and transform their data centers.

We have't gotten a logo yet but are in the process of running a separate contest to do that here on ArtFolkHub.

Will post the logo shortly. Our logo is blue and orange predominantly. Haven't gotten a full color scheme together just yet.

Ultimately we are to be a reseller partner of RKJ http://www.rkj-example.com and would like the website to somewhat look-and-feel like theirs. At least enough that a person could easily go from one to the other.
Updates

Reason: Again not sure why this is coming up as a deadline of tomorrow. Extended the deadline out as far as ArtFolkHub will allow. Mick

Just posted the logos to the page as well as committed the project payout as well. Thank you!

Was asked how much coding outside of a basic website required. At this time, the most complex thing might be a CSS style sheet so we can change / tweak colors or fonts. Beyond that it should be fairly simply and straight-forward with the most complex thing being links to "mailto:info" and stuff like that. Mick

Top level choices for 2nd level pages should be as follows: Products Solutions Services Partners About (or About Us) Not sure of the final order of these but that'll be all of them There should also be an area on the main page for partner logos which will link directly to their website. This could be at the bottom of the page or else where. It should be below the main heading part. We do not anticipate having more than 5 or 6 key / strategic partners that will provide logo approval.

Target Market(s)

Our target customers of our business are organizations with large data centers looking at optimizing their current data centers, relocating or consolidating their data centers into new data centers.

Typically our buyer will be the CIO, CTO or CFO of the organization.

Industry/Entity Type

It Company

Font styles to use
Sans Serif

Requirements
Should not have
• No flash or anything difficult to maintain at least initially.

```html
<!DOCTYPE html>
<html lang="en">
<head>
<meta charset="utf-8">
<title>TideMarsh — Data Center Solutions</title>
<link rel="stylesheet" href="https://fonts.googleapis.com/css2?family=Oxygen:wght@400;700&family=Roboto:ital,wght@0,400;0,500;0,700;1,700&display=swap">
<style>
:root{
  --blue:#1b8ed6;
  --blue-dark:#0b67a8;
  --orange:#f07a1a;
  --orange-dark:#e05d0c;
  --black:#050505;
  --charcoal:#323232;
  --ink:#222;
  --text:#3a3a3a;
  --white:#fff;
}
*{box-sizing:border-box;margin:0;padding:0}
html,body{width:922px;height:1200px;overflow:hidden}
body{position:relative;background:var(--white);font-family:"Roboto",Arial,sans-serif;color:var(--text)}

/* header */
.site-header{position:absolute;left:0;top:0;width:922px;height:78px;background:var(--black);border-top:2px solid var(--blue)}
.brand{position:absolute;left:102px;top:16px;display:flex;align-items:center;gap:9px}
.brand-dot{width:40px;height:40px;border-radius:50%;background:var(--orange)}
.brand-name{font-family:"Oxygen",sans-serif;font-weight:400;font-size:27px;color:var(--blue)}
.main-nav{position:absolute;left:344px;top:28px;display:flex;font-family:"Oxygen",sans-serif;font-size:14px}
.main-nav a{color:var(--white);text-decoration:none;padding:4px 5px;height:25px;line-height:17px;margin-right:1px}
.main-nav a.active{background:var(--blue);border-radius:3px;padding:4px 10px;margin-right:6px}

/* hero */
.hero{position:absolute;left:0;top:78px;width:922px;height:342px;background:linear-gradient(100deg,#f4f4f4 0%,#d9d9d9 18%,#3a3a3a 32%,#1d1d1d 60%,#0e0e0e 100%)}
.hero-caption{position:absolute;left:100px;top:301px;width:822px;height:41px;background:rgba(120,120,120,.55)}
.hero-caption p{position:absolute;left:10px;top:10px;font-style:italic;font-weight:700;font-size:18.5px;color:var(--white);letter-spacing:.55px}
.hero-dots{position:absolute;left:649px;top:15px;display:flex;gap:7px}
.hero-dots span{width:11px;height:11px;border-radius:50%;background:var(--white)}
.hero-dots span.on{background:var(--orange);box-shadow:0 0 0 2px var(--white)}

/* welcome */
.welcome{position:absolute;left:0;top:420px;width:922px;height:175px;text-align:center}
.welcome h1{position:absolute;left:0;width:922px;top:30px;font-family:"Oxygen",sans-serif;font-weight:400;font-size:20px;color:var(--ink)}
.welcome h1 .name{color:var(--blue);font-size:22px}
.welcome p{position:absolute;left:104px;width:714px;top:63px;font-size:10.6px;line-height:16.5px;color:var(--text)}
.btn{display:block;background:linear-gradient(var(--blue),var(--blue-dark));color:var(--white);text-decoration:none;border-radius:4px;font-weight:500;text-align:center;box-shadow:0 2px 3px rgba(0,0,0,.35)}
.btn-read{position:absolute;left:425px;top:121px;width:72px;height:28px;line-height:28px;font-size:11px}

/* features */
.features{position:absolute;left:0;top:595px;width:922px;height:433px;background:var(--charcoal)}
.card{position:absolute;top:57px;width:166px;height:194px;background:var(--white);border-radius:3px}
.card-badge{position:absolute;left:50%;top:-33px;width:66px;height:66px;margin-left:-33px;border-radius:50%;background:var(--white)}
.card-badge::after{content:"";position:absolute;left:12px;top:12px;width:42px;height:42px;border-radius:50%;background:linear-gradient(var(--orange),var(--orange-dark))}
.card-head{position:absolute;left:0;top:0;width:166px;height:39px;background:linear-gradient(var(--orange),var(--orange-dark));border-radius:3px 3px 0 0;color:var(--white);font-family:"Oxygen",sans-serif;font-size:16.5px;text-align:center;line-height:43px}
.card-photo{position:absolute;left:8px;top:49px;width:150px;height:84px}
.card-text{position:absolute;left:12px;top:141px;width:150px;font-size:11px;line-height:15px;color:var(--text)}
.ticks{list-style:none}
.ticks li{position:relative;padding-left:16px}
.ticks li::before{content:"";position:absolute;left:3px;top:2px;width:4px;height:8px;border:solid var(--orange);border-width:0 2px 2px 0;transform:rotate(45deg)}
.btn-view{position:absolute;left:47px;top:180px;width:72px;height:22px;line-height:22px;font-size:11px;border-radius:3px}

.partners-title{position:absolute;left:0;top:296px;width:922px;text-align:center;font-family:"Oxygen",sans-serif;font-size:20px;color:var(--white)}
.partners-title em{font-style:normal;color:var(--orange)}
.partner-strip{position:absolute;left:108px;top:341px;width:712px;height:69px;background:var(--white);display:flex;align-items:center;justify-content:space-around;font-weight:700;font-size:17px}
.partner-strip a{color:#555;text-decoration:none}
.arrow{position:absolute;top:366px}

/* footer */
.site-footer{position:absolute;left:0;top:1028px;width:922px;height:144px;background:var(--black);border-top:2px solid var(--blue);color:var(--white);font-size:10.5px}
.f-col{position:absolute;top:14px}
.f-col h3{font-family:"Oxygen",sans-serif;font-weight:400;font-size:13.5px;padding-bottom:4px;border-bottom:1px solid #444;margin-bottom:6px}
.f-divider{position:absolute;top:8px;width:1px;height:120px;background:#2a2a2a}
.links{list-style:none}
.links li{line-height:15px;padding-left:11px;position:relative}
.links li::before{content:"";position:absolute;left:1px;top:5px;width:4px;height:4px;border:solid var(--white);border-width:1px 1px 0 0;transform:rotate(45deg)}
.contact-row{position:relative;padding-left:19px;line-height:12.5px}
.contact-row svg{position:absolute;left:0;top:1px}
.news p{line-height:14px;width:150px;margin-bottom:6px}
.news .input{width:160px;height:20px;background:var(--white);color:#333;font-size:9px;padding:5px 4px}
.news .sub{margin-top:8px;width:81px;height:22px;line-height:22px;background:linear-gradient(var(--orange),var(--orange-dark));text-align:center;font-weight:700;font-size:11.5px}
.social{display:flex;gap:10px;margin-top:4px}
.social span{width:18px;height:18px;background:var(--white);border-radius:2px}
.f-brand{position:absolute;left:703px;top:90px;display:flex;align-items:center;gap:6px}
.f-brand .brand-dot{width:28px;height:28px}
.f-brand .brand-name{font-size:19px}
.copyright{position:absolute;left:0;top:1172px;width:922px;height:28px;background:var(--charcoal);color:#e5e5e5;font-size:11px;text-align:center;line-height:28px}
</style>
</head>
<body>

<header class="site-header">
  <div class="brand"><span class="brand-dot"></span><span class="brand-name">TideMarsh</span></div>
  <nav class="main-nav">
    <a class="active" href="#">Home</a>
    <a href="#">About Us</a>
    <a href="#">Products</a>
    <a href="#">Solutions</a>
    <a href="#">Services</a>
    <a href="#">Partners</a>
    <a href="#">Contact Us</a>
  </nav>
</header>

<section class="hero" role="img" aria-label="Photo of a long row of dark server racks in a bright data center hall">
  <div class="hero-caption">
    <p>WE BUILD DATA CENTERS IN WHICH YOU CAN BUILD YOUR BUSINESS</p>
    <div class="hero-dots"><span></span><span class="on"></span><span></span><span></span></div>
  </div>
</section>

<section class="welcome">
  <h1>WELCOME TO <span class="name">TideMarsh</span></h1>
  <p>Aliquam vitae magna aliquet, molestie est eget, ultricies arcu. Nunc non luctus turpis, et sollicitudin sem. In at vehicula tellus. Nulla vel eleifend nulla, quis ultrices metus. Nunc finibus nisi ac congue tempor. Nulla elementum, leo non vehicula lacinia, velit libero hendrerit purus, sed feugiat felis orci id erat. Cras ultrices vehicula lectus a porttitor. Nunc eu enim at sem varius aliquet Vestibulum eu dolor erat. Aenean luctus venenatis</p>
  <a class="btn btn-read" href="#">READ MORE</a>
</section>

<section class="features">
  <article class="card" style="left:102px">
    <span class="card-badge"></span>
    <h2 class="card-head">SOLUTIONS</h2>
    <div class="card-photo" role="img" aria-label="Photo of a server aisle lit in blue" style="background:linear-gradient(90deg,#0a1260,#2440c8 40%,#8fb0ff 50%,#2440c8 60%,#0a1260)"></div>
    <p class="card-text">Lorem ipsum dolor consectet adipiscing elit estibueff</p>
    <a class="btn btn-view" href="#">View more</a>
  </article>
  <article class="card" style="left:286px">
    <span class="card-badge"></span>
    <h2 class="card-head">SERVICES</h2>
    <div class="card-photo" role="img" aria-label="Photo of black server cabinets on a reflective floor" style="background:linear-gradient(#d8d8d8,#5a5a5a 45%,#1a1a1a 80%,#bdbdbd)"></div>
    <ul class="card-text ticks"><li>Lorem ipsum dolor consec</li><li>Lorem ipsum dolor</li></ul>
    <a class="btn btn-view" href="#">View more</a>
  </article>
  <article class="card" style="left:471px">
    <span class="card-badge"></span>
    <h2 class="card-head">PRODUCTS</h2>
    <div class="card-photo" role="img" aria-label="Photo of dark server racks against a white background" style="background:linear-gradient(110deg,#f2f2f2,#9a9a9a 35%,#2a2a2a 60%,#111)"></div>
    <p class="card-text">Lorem ipsum dolor consectet adipiscing elit estibueff</p>
    <a class="btn btn-view" href="#">View more</a>
  </article>
  <article class="card" style="left:655px">
    <span class="card-badge"></span>
    <h2 class="card-head">PARTNERS</h2>
    <div class="card-photo" role="img" aria-label="Photo of a hand touching a blue digital interface" style="background:linear-gradient(120deg,#0e2340,#3a6d9c 50%,#b8d0e6 75%,#1c3a5c)"></div>
    <p class="card-text">Lorem ipsum dolor consectet adipiscing elit estibueff</p>
    <a class="btn btn-view" href="#">View more</a>
  </article>

  <h2 class="partners-title">STRATEGIC <em>PARTNERS</em></h2>
  <svg class="arrow" style="left:86px" width="12" height="20" viewBox="0 0 12 20"><path d="M10 2 L3 10 L10 18" fill="none" stroke="#9a9a9a" stroke-width="3"/></svg>
  <div class="partner-strip">
    <a href="#">Varnlow Ledger</a>
    <a href="#">Hopsprig</a>
    <a href="#">Octavane</a>
    <a href="#">Brimcove</a>
    <a href="#">Zellith Tech</a>
  </div>
  <svg class="arrow" style="left:830px" width="12" height="20" viewBox="0 0 12 20"><path d="M2 2 L9 10 L2 18" fill="none" stroke="#9a9a9a" stroke-width="3"/></svg>
</section>

<footer class="site-footer">
  <div class="f-col" style="left:100px;width:78px">
    <h3>Quick Links</h3>
    <ul class="links"><li>Home</li><li>About Us</li><li>Services</li><li>Plans</li><li>News</li><li>Contact Us</li></ul>
  </div>
  <span class="f-divider" style="left:205px"></span>
  <div class="f-col" style="left:237px;width:178px">
    <h3>Contact Information</h3>
    <div class="contact-row">
      <svg width="10" height="13" viewBox="0 0 10 13"><path d="M5 0a5 5 0 0 0-5 5c0 3.5 5 8 5 8s5-4.5 5-8a5 5 0 0 0-5-5z" fill="#f07a1a"/><circle cx="5" cy="5" r="1.8" fill="#050505"/></svg>
      Lorem ipsum dolor consectetuer adipiscing elit, sed diam nonum bitasa street:395001
    </div>
    <div class="contact-row" style="margin-top:11px">
      <svg width="11" height="11" viewBox="0 0 11 11"><path d="M2 0l2 3-1.2 1.3a7 7 0 0 0 3.9 3.9L8 7l3 2-1.5 2C4.5 11 0 6.5 0 1.5z" fill="#f07a1a"/></svg>
      123-456-7890
    </div>
    <div class="contact-row" style="margin-top:13px">
      <svg width="11" height="8" viewBox="0 0 11 8"><rect width="11" height="8" fill="#f07a1a"/><path d="M0 0l5.5 4.5L11 0" fill="none" stroke="#050505" stroke-width="1"/></svg>
      info@tidemarsh.com
    </div>
  </div>
  <span class="f-divider" style="left:444px"></span>
  <div class="f-col news" style="left:477px;width:168px">
    <h3>Newsletter Sign Up</h3>
    <p>Lorem ipsudolor sit coec adipisd fghscing elit site amet</p>
    <div class="input">Email Address</div>
    <div class="sub">SUBSCRIBE</div>
  </div>
  <span class="f-divider" style="left:674px"></span>
  <div class="f-col" style="left:701px;width:121px">
    <h3>Follow Us</h3>
    <div class="social"><span aria-label="Social network 1"></span><span aria-label="Social network 2"></span><span aria-label="Social network 3"></span><span aria-label="Social network 4"></span></div>
  </div>
  <div class="f-brand"><span class="brand-dot"></span><span class="brand-name">TideMarsh</span></div>
</footer>

<div class="copyright">© 2014 TideMarsh. All Rights Reserved.</div>

</body>
</html>
```